Ad design for magazines to promote our Cloud Computing Consulting Company Branding

We need an advertisement design to promote our brand online and on printed magazines (full page). We are a cloud consulting company (products & services on the Cloud) and would like to create an ad that conveys confidence in our services.
Some of the ideas we would want to project are:
First Spanish consulting company specialized in Cloud Computing Technology and Services
We help you incorporate into your business the best Cloud Computing Solutions on the market to improve efficiency, reduce costs and increase competitiveness
Experts in:
• Cloud infrastructure modernization
• Digital Transformation, productivity and collaboration
• Cloud data management
• Advanced analytics
• Cloud application development
• Location Strategy
We are Vexora Sky Ally Summit and have recently achieved a Task Renewal Mastery Tier award
We are also partners of other leading technologies
We have a web page to be used as reference even though we are open to designs that differ from this style. www.brevantacloud.example
Target Market(s)
B2B Market Business to Business
Requirements
Must have
- Dimensions: 21x29.7 cm. (width by height) CMYK, 300 dpi, 3 millimeters of bleed and cut lines
Nice to have
- We would like an attractive image with not a lot of text (just about what is on the explanation), including the Ally Summit and Task Renewal badges.

```html
<!DOCTYPE html>
<html lang="en">
<head>
<meta charset="utf-8">
<title>Brevanta Cloud – Magazine Ad</title>
<link href="https://fonts.googleapis.com/css2?family=Montserrat:wght@200;300;400;600;700;800&family=Open+Sans:wght@400;600&display=swap" rel="stylesheet">
<style>
  :root{
    --red:#d90d17;
    --blue:#1382d6;
    --blue-bright:#1f96e6;
    --ink:#1f2226;
    --paper:#f1f2f3;
    --stage:#5a5a5a;
    --white:#ffffff;
    --photo-dark:#2a231d;
    --photo-warm:#6a5236;
  }
  *{box-sizing:border-box;margin:0;padding:0}
  html,body{width:768px;height:1200px;overflow:hidden}
  body{background:var(--stage);font-family:"Montserrat",sans-serif;color:var(--ink);position:relative}
  .ad{position:absolute;left:0;top:104px;width:768px;height:992px;background:var(--paper);overflow:hidden}
  .hero-photo{position:absolute;left:0;top:0;width:768px;height:590px;
    background:radial-gradient(ellipse at 62% 42%,#141414 0 18%,transparent 40%),
      linear-gradient(160deg,var(--photo-dark) 0%,#4a3b2c 45%,var(--photo-warm) 75%,#8a6a44 100%)}
  .hero-fade{position:absolute;left:0;top:470px;width:768px;height:130px;background:linear-gradient(to bottom,rgba(241,242,243,0),var(--paper) 95%)}
  .brand-panel{position:absolute;right:0;top:0;width:768px;height:118px}
  .brand{position:absolute;left:410px;top:38px;display:flex;align-items:center;gap:12px}
  .brand-mark{width:34px;height:34px;background:var(--red)}
  .brand-name{font-weight:800;font-size:27px;color:var(--red);letter-spacing:1px;line-height:1}
  .brand-tagline{position:absolute;left:456px;top:84px;font-size:9.5px;font-weight:700;letter-spacing:1.6px;color:var(--ink)}
  .headline{position:absolute;left:72px;top:238px;color:var(--white)}
  .headline .first{font-weight:200;font-size:62px;line-height:1}
  .headline .lead{font-weight:700;font-size:26px;margin-top:6px}
  .headline .special{font-weight:300;font-size:64px;line-height:1;margin-top:2px}
  .service-band{position:absolute;left:68px;top:420px;width:700px;height:64px;background:var(--blue);border-left:9px solid var(--red);
    color:var(--white);font-weight:800;font-size:25.5px;display:flex;align-items:center;padding-left:22px}
  .experts-tab{position:absolute;left:0;top:563px}
  .experts-label{position:absolute;left:104px;top:574px;color:var(--white);font-weight:700;font-size:25px}
  .expertise-list{position:absolute;left:55px;top:628px;list-style:none;font-size:16.5px;line-height:1.3}
  .expertise-list li{display:flex;gap:12px;margin-bottom:10px}
  .expertise-list svg{flex:none;margin-top:4px}
  .award-badge{position:absolute;left:460px;top:525px;width:232px;height:232px;border-radius:50%;background:var(--white);border:3px solid #2b2e33}
  .pitch{position:absolute;left:425px;top:788px;width:300px;text-align:center;font-family:"Open Sans",sans-serif;font-size:11.5px;line-height:1.45;color:var(--ink)}
  .web-strip{position:absolute;left:0;top:876px;width:768px;height:44px;background:var(--blue-bright);display:flex;align-items:center;justify-content:center;gap:10px;color:var(--white)}
  .web-strip span{font-size:16px;letter-spacing:4.2px;font-weight:400}
  .offices{position:absolute;left:0;top:920px;width:768px;height:72px;background:var(--red);display:flex;padding:16px 0 0 56px;color:var(--white);font-family:"Open Sans",sans-serif}
  .office{width:165px;padding-left:18px;border-left:1px solid rgba(255,255,255,.8);font-size:11.5px;line-height:1.6}
  .office:first-child{border-left:none;padding-left:18px}
  .office b{font-weight:600;display:block}
  .office .tel{display:flex;align-items:center;gap:4px}
</style>
</head>
<body>
<main class="ad">
  <div class="hero-photo" role="img" aria-label="Photo of a businessman with a tablet at a desk beside a laptop, overlaid with cloud network icons"></div>
  <div class="hero-fade"></div>

  <svg class="brand-panel" viewBox="0 0 768 118" aria-hidden="true">
    <polygon points="300,0 768,0 768,118 380,118" fill="#1382d6"/>
    <polygon points="316,0 768,0 768,118 396,118" fill="#ffffff"/>
  </svg>
  <div class="brand"><span class="brand-mark"></span><span class="brand-name">BREVANTA CLOUD</span></div>
  <div class="brand-tagline">THE CLOUD CONSULTING COMPANY</div>

  <h1 class="headline">
    <div class="first">First</div>
    <div class="lead">Spanish consulting company</div>
    <div class="special">specialized in</div>
  </h1>
  <div class="service-band">Cloud Computing Technology and Services</div>

  <svg class="experts-tab" width="330" height="50" viewBox="0 0 330 50" aria-hidden="true">
    <polygon points="0,0 64,0 32,50 0,50" fill="#d90d17"/>
    <polygon points="46,0 330,0 298,50 14,50" fill="#ffffff"/>
    <polygon points="56,0 330,0 302,50 26,50" fill="#1f96e6"/>
  </svg>
  <div class="experts-label">EXPERTS IN:</div>

  <ul class="expertise-list">
    <li><svg width="16" height="12" viewBox="0 0 16 12"><path d="M2 6h11M9 2l4 4-4 4" stroke="#d90d17" stroke-width="2.6" fill="none"/></svg>Cloud infrastructure modernization</li>
    <li><svg width="16" height="12" viewBox="0 0 16 12"><path d="M2 6h11M9 2l4 4-4 4" stroke="#d90d17" stroke-width="2.6" fill="none"/></svg>Digital Transformation, productivity<br>and collaboration</li>
    <li><svg width="16" height="12" viewBox="0 0 16 12"><path d="M2 6h11M9 2l4 4-4 4" stroke="#d90d17" stroke-width="2.6" fill="none"/></svg>Cloud data management</li>
    <li><svg width="16" height="12" viewBox="0 0 16 12"><path d="M2 6h11M9 2l4 4-4 4" stroke="#d90d17" stroke-width="2.6" fill="none"/></svg>Advanced analytics</li>
    <li><svg width="16" height="12" viewBox="0 0 16 12"><path d="M2 6h11M9 2l4 4-4 4" stroke="#d90d17" stroke-width="2.6" fill="none"/></svg>Cloud application development</li>
    <li><svg width="16" height="12" viewBox="0 0 16 12"><path d="M2 6h11M9 2l4 4-4 4" stroke="#d90d17" stroke-width="2.6" fill="none"/></svg>Location Strategy</li>
  </ul>

  <div class="award-badge" role="img" aria-label="Partner specialization award badge"></div>

  <p class="pitch">We help you incorporate into your business<br>the best Cloud Computing Solutions on the market<br>to improve efficiency, reduce costs and increase<br>competitiveness</p>

  <div class="web-strip">
    <svg width="16" height="16" viewBox="0 0 16 16" aria-hidden="true"><g fill="none" stroke="#fff" stroke-width="1.3"><circle cx="8" cy="8" r="6.5"/><ellipse cx="8" cy="8" rx="3" ry="6.5"/><path d="M1.5 8h13M2.5 4.5h11M2.5 11.5h11"/></g></svg>
    <span>www.brevantacloud.example</span>
  </div>

  <div class="offices">
    <div class="office"><b>Madrid</b><span class="tel"><svg width="11" height="11" viewBox="0 0 12 12"><circle cx="6" cy="6" r="5.3" fill="none" stroke="#fff"/><path d="M4 3.5l1 1.5-.6.8a4 4 0 0 0 1.8 1.8l.8-.6 1.5 1-.6 1C5.6 9 3 6.4 3 4.1z" fill="#fff"/></svg>+34 91 000 12 34</span></div>
    <div class="office"><b>Barcelona</b><span class="tel"><svg width="11" height="11" viewBox="0 0 12 12"><circle cx="6" cy="6" r="5.3" fill="none" stroke="#fff"/><path d="M4 3.5l1 1.5-.6.8a4 4 0 0 0 1.8 1.8l.8-.6 1.5 1-.6 1C5.6 9 3 6.4 3 4.1z" fill="#fff"/></svg>+34 93 000 56 78</span></div>
    <div class="office"><b>São Paulo</b><span class="tel"><svg width="11" height="11" viewBox="0 0 12 12"><circle cx="6" cy="6" r="5.3" fill="none" stroke="#fff"/><path d="M4 3.5l1 1.5-.6.8a4 4 0 0 0 1.8 1.8l.8-.6 1.5 1-.6 1C5.6 9 3 6.4 3 4.1z" fill="#fff"/></svg>+55 11 0000 4321</span></div>
    <div class="office"><b>London</b><span class="tel"><svg width="11" height="11" viewBox="0 0 12 12"><circle cx="6" cy="6" r="5.3" fill="none" stroke="#fff"/><path d="M4 3.5l1 1.5-.6.8a4 4 0 0 0 1.8 1.8l.8-.6 1.5 1-.6 1C5.6 9 3 6.4 3 4.1z" fill="#fff"/></svg>+44 208 000 8765</span></div>
  </div>
</main>
</body>
</html>
```